Vendra Q7 - DL Flyer

Flyer designed with the following points:

Retail Point of Sale
Hardware and Software
Highly customisable to suit your business
Free POS appraisal and Quotes
E-commerce Integrations with your existing website
Multiple Store Capability
One on one set up and support
100% Tax Deductable
From only $9.95 per week

1300 462 718
admin@vendraq7.com.au
www.vendraq7.com.au

```html
<!DOCTYPE html>
<html lang="en">
<head>
<meta charset="utf-8">
<title>Vendra Q7 – DL Flyer</title>
<link rel="stylesheet" href="https://fonts.googleapis.com/css2?family=Michroma&family=Roboto:wght@400;500;700&display=swap">
<style>
  :root {
    --brand-blue: #1ea8e0;
    --paper: #f5f5f3;
    --ink: #231f20;
    --white: #ffffff;
    --page: #ffffff;
  }
  * { box-sizing: border-box; margin: 0; padding: 0; }
  html, body { width: 1027px; height: 1200px; overflow: hidden; background: var(--page); }
  body { position: relative; font-family: "Roboto", Arial, sans-serif; color: var(--ink); }

  .flyer {
    position: absolute;
    top: 243px;
    width: 312px;
    height: 663px;
    background: var(--paper);
    overflow: hidden;
  }
  .flyer--features { left: 138px; }
  .flyer--pricing { left: 516px; }

  /* Features side */
  .top-tab {
    position: absolute; left: 36px; top: 0; width: 241px; height: 31px;
    background: var(--brand-blue);
    border-radius: 0 0 26px 26px;
  }
  .brand {
    position: absolute; top: 38px; left: 0; width: 100%;
    display: flex; justify-content: center; align-items: center; gap: 6px;
    font-weight: 700; font-size: 25px; color: var(--brand-blue); letter-spacing: 0.3px;
  }
  .brand__dot { width: 12px; height: 12px; border-radius: 50%; background: var(--brand-blue); }

  .band { position: absolute; left: 0; width: 100%; height: 13px; background: var(--brand-blue); }

  .feature {
    position: absolute; left: 0; width: 100%;
    display: flex; align-items: center;
    padding-left: 46px; padding-right: 16px;
    font-size: 15px; font-weight: 500; line-height: 1.3;
  }
  .feature::before {
    content: ""; position: absolute; left: 29px; top: 50%;
    width: 8px; height: 8px; margin-top: -4px;
    border-radius: 50%; background: var(--brand-blue);
  }

  .phone {
    position: absolute; top: 545px; left: 0; width: 100%; text-align: center;
    font-family: "Michroma", sans-serif; font-size: 20px; color: var(--brand-blue);
    letter-spacing: 0.5px;
  }
  .contact-footer {
    position: absolute; left: 0; top: 587px; width: 100%; height: 76px;
    background: var(--brand-blue); color: var(--white);
    text-align: center; font-size: 20px; line-height: 28px; padding-top: 7px;
  }
  .footer-tab {
    position: absolute; left: 99px; bottom: -10px; width: 143px; height: 20px;
    background: var(--white); border-radius: 20px 20px 0 0;
  }

  /* Pricing side */
  .top-connector {
    position: absolute; left: 129px; top: 0; width: 71px; height: 14px; background: var(--brand-blue);
  }
  .tier { position: absolute; left: 0; width: 100%; height: 160px; }
  .tier__frame {
    position: absolute; left: 0; top: 29px; width: 100%; height: 116px;
    border: 7px solid var(--brand-blue); border-bottom: none;
    border-radius: 26px 26px 0 0;
  }
  .tier__label {
    position: absolute; left: 69px; top: 13px; width: 177px; height: 39px;
    background: var(--brand-blue); color: var(--white);
    border-radius: 20px; text-align: center;
    font-family: "Michroma", sans-serif;
  }
  .tier__name { display: block; font-size: 12.5px; line-height: 14px; padding-top: 6px; }
  .tier__sub { display: block; font-size: 6.5px; line-height: 9px; letter-spacing: 0.2px; }

  .price {
    position: absolute; left: 0; top: 58px; width: 100%;
    display: flex; justify-content: center; align-items: flex-start;
    font-family: "Michroma", sans-serif; color: var(--ink);
  }
  .price__currency { font-size: 13px; margin-top: 6px; margin-right: 3px; }
  .price__whole { font-size: 44px; line-height: 44px; font-weight: 700; letter-spacing: -2px; }
  .price__cents { font-size: 15px; margin-top: 2px; margin-left: 3px; }
  .price__period {
    position: absolute; left: 0; top: 107px; width: 100%; text-align: center;
    font-family: "Michroma", sans-serif; font-size: 14.5px; color: var(--ink);
  }

  .tier__specs {
    position: absolute; left: 0; top: 138px; width: 100%; height: 22px;
    background: var(--brand-blue); color: var(--white);
    display: flex; justify-content: space-between; align-items: center;
    padding: 0 19px 0 16px; font-size: 10.5px;
  }
  .tier__specs .sep { opacity: 0.9; }

  .tax-note {
    position: absolute; left: 0; top: 629px; width: 100%; text-align: center;
    color: var(--brand-blue); font-weight: 700; font-size: 10px; line-height: 11px;
    z-index: 2;
  }
  .base-band { position: absolute; left: 0; top: 647px; width: 100%; height: 16px; background: var(--brand-blue); }
  .base-notch { position: absolute; left: 89px; top: 647px; width: 134px; height: 6px; }
</style>
</head>
<body>

<section class="flyer flyer--features" aria-label="Vendra Q7 features">
  <div class="top-tab"></div>
  <div class="brand"><span>VENDRA Q7</span><span class="brand__dot"></span></div>

  <div class="band" style="top:74px"></div>
  <div class="feature" style="top:87px;height:36px">Hardware and Software</div>
  <div class="band" style="top:123px"></div>
  <div class="feature" style="top:136px;height:61px">Highly customisable to suit your business</div>
  <div class="band" style="top:197px"></div>
  <div class="feature" style="top:210px;height:39px">Free POS appraisal and Quotes</div>
  <div class="band" style="top:249px"></div>
  <div class="feature" style="top:262px;height:58px">E-commerce Integrations with your existing website</div>
  <div class="band" style="top:320px"></div>
  <div class="feature" style="top:333px;height:40px">Multiple Store Capability</div>
  <div class="band" style="top:373px"></div>
  <div class="feature" style="top:386px;height:38px">One on one set up and support</div>
  <div class="band" style="top:424px"></div>
  <div class="feature" style="top:437px;height:40px">100% Tax Deductable</div>
  <div class="band" style="top:477px"></div>
  <div class="feature" style="top:490px;height:42px">From only $9.95 per week</div>
  <div class="band" style="top:532px"></div>

  <div class="phone">1300 462 718</div>
  <div class="contact-footer">
    <div>admin@vendraq7.com.au</div>
    <div>www.vendraq7.com.au</div>
    <div class="footer-tab"></div>
  </div>
</section>

<section class="flyer flyer--pricing" aria-label="Vendra Q7 pricing">
  <div class="top-connector"></div>

  <div class="tier" style="top:0">
    <div class="tier__frame"></div>
    <div class="tier__label"><span class="tier__name">SMALL RETAIL</span><span class="tier__sub">SOFTWARE PACKAGE</span></div>
    <div class="price"><span class="price__currency">$</span><span class="price__whole">9</span><span class="price__cents">95</span></div>
    <div class="price__period">PER WEEK</div>
    <div class="tier__specs"><span>1-2 Staff Users</span><span class="sep">|</span><span>1 Cash Register</span><span class="sep">|</span><span>1 Store Location</span></div>
  </div>

  <div class="tier" style="top:156px">
    <div class="tier__frame"></div>
    <div class="tier__label"><span class="tier__name">SMALL RETAIL</span><span class="tier__sub">SOFTWARE PACKAGE</span></div>
    <div class="price"><span class="price__currency">$</span><span class="price__whole">17</span><span class="price__cents">95</span></div>
    <div class="price__period">PER WEEK</div>
    <div class="tier__specs"><span>3-8 Staff Users</span><span class="sep">|</span><span>2-3 Cash Register</span><span class="sep">|</span><span>1 Store Location</span></div>
  </div>

  <div class="tier" style="top:312px">
    <div class="tier__frame"></div>
    <div class="tier__label"><span class="tier__name">SMALL RETAIL</span><span class="tier__sub">SOFTWARE PACKAGE</span></div>
    <div class="price"><span class="price__currency">$</span><span class="price__whole">34</span><span class="price__cents">95</span></div>
    <div class="price__period">PER WEEK</div>
    <div class="tier__specs"><span>8-20 Staff Users</span><span class="sep">|</span><span>2-10 Cash Register</span><span class="sep">|</span><span>1 Store Location</span></div>
  </div>

  <div class="tier" style="top:468px">
    <div class="tier__frame"></div>
    <div class="tier__label"><span class="tier__name">SMALL RETAIL</span><span class="tier__sub">SOFTWARE PACKAGE</span></div>
    <div class="price"><span class="price__currency">$</span><span class="price__whole">49</span><span class="price__cents">95</span></div>
    <div class="price__period">PER WEEK</div>
    <div class="tier__specs"><span>20+ Staff Users</span><span class="sep">|</span><span>10+ Cash Register</span><span class="sep">|</span><span>2-3 Store Location</span></div>
  </div>

  <div class="base-band"></div>
  <svg class="base-notch" viewBox="0 0 134 6" aria-hidden="true"><polygon points="0,0 134,0 128,6 6,6" fill="var(--paper)"/></svg>
  <div class="tax-note">100% TAX DEDUCTIBLE<br>(Invoiced Monthly)</div>
</section>

</body>
</html>
```